WordPress Website for Pain Relief Clinic

I need a WordPress website designed for my laser pain relief clinic. It needs to be a professional, responsive design with 7 pages: Home, Why Choose Us, Treatable Conditions, Testimonials, FAQ, Franchising, Contact Us. Here is logo: https://files.brivoltcdn.com/media.t-w-e-n.com/sitebuilder/472/CalvexaLogoHighQuality.png

Target Market(s)

people with pain,elderly adults,injuries,soreness

Industry/Entity Type

Clinic

Number of Pages Required

5+ page

Colors
0792cd
85abd2

```html
<!DOCTYPE html>
<html lang="en">
<head>
<meta charset="utf-8">
<title>Calvexa</title>
<link href="https://fonts.googleapis.com/css2?family=Cinzel:wght@400;700&family=Arimo:ital,wght@0,400;0,700;1,400&family=Roboto+Condensed:wght@400&family=Roboto+Slab:wght@400&display=swap" rel="stylesheet">
<style>
:root{
  --teal:#2ba6a0;
  --ink:#2f2f2f;
  --text:#4a4a4a;
  --line:#c9c9c9;
  --footer:#383838;
  --footer-text:#e6e6e6;
  --footer-brand:#9a9a9a;
  --white:#fff;
}
*{box-sizing:border-box;margin:0;padding:0}
html,body{width:675px;height:1200px;overflow:hidden;background:var(--white)}
body{position:relative;font-family:"Arimo",Arial,sans-serif;color:var(--text)}
.abs{position:absolute}

/* header */
.brand{left:30px;top:20px;display:flex;align-items:center;gap:8px;font-family:"Arimo",Arial,sans-serif;font-weight:700;font-size:25px;line-height:28px;color:var(--ink)}
.brand-dot{width:14px;height:14px;border-radius:50%;background:var(--teal)}
.book-btn{left:342px;top:25px;width:175px;height:23px;background:var(--ink);color:var(--white);font-family:"Cinzel",serif;font-size:11.5px;display:flex;align-items:center;justify-content:center;border-radius:2px}
.call{left:543px;top:22px;display:flex;gap:6px;align-items:center}
.call-text{font-size:10.5px;color:var(--ink);line-height:13px}
.call-text b{display:block;font-weight:400;font-size:13px}

/* nav */
.nav{left:0;top:64px;width:675px;height:25px;background:var(--teal)}
.nav a{position:absolute;top:0;height:25px;line-height:25px;font-family:"Cinzel",serif;font-size:9.6px;color:var(--white);text-decoration:none;padding:0 8px;border-right:1px solid rgba(255,255,255,.25)}
.nav a.active{background:#247f7a;color:#1b3b3a}

/* hero */
.hero{left:0;top:89px;width:675px;height:218px;background:linear-gradient(120deg,#1d1a18 0%,#4a3b33 40%,#6b5244 55%,#2a2320 100%)}
.hero-title{left:36px;top:264px;font-family:"Cinzel",serif;font-size:26px;font-weight:400;color:var(--white)}
.hours{left:482px;top:253px;width:149px;height:47px;background:var(--white);padding:4px 6px;font-size:8px;line-height:12px;color:var(--ink)}
.hours h4{font-size:8.5px;font-weight:700;border-bottom:1px dashed var(--line);padding-bottom:2px;margin-bottom:2px}
.hours p{font-style:italic}

/* quick band */
.band{left:0;top:307px;width:675px;height:59px;background:var(--teal)}
.band-item{color:var(--white);font-size:11.5px;line-height:14px}
.band-item.serif{font-family:"Roboto Slab",serif}

/* about */
.h2{font-family:"Cinzel",serif;font-size:19px;color:var(--ink)}
.h2 .first{color:var(--teal)}
.rule{border-bottom:1px dashed var(--line)}
.about-copy{left:38px;top:427px;width:144px;font-size:8.3px;line-height:10.9px}
.about-copy p+p{margin-top:3px}
.photo{top:402px;width:137px;height:100px}
.service-title{top:508px;width:137px;font-family:"Cinzel",serif;font-size:13px;color:var(--ink);padding-bottom:2px}
.service-title span{color:var(--teal)}
.service-text{top:528px;width:137px;font-size:8.3px;line-height:11.6px}
.more{top:594px;font-size:8.3px;color:var(--ink)}
.divider{left:40px;top:624px;width:595px;height:1px;background:linear-gradient(90deg,transparent,#ddd,transparent)}

/* inquiry */
.sub{font-size:8.3px;color:var(--ink)}
.label{font-size:8.3px;font-style:italic;color:var(--text)}
.field{border:1px solid #d4d4d4;background:var(--white);font-size:8.3px;font-style:italic;color:var(--text);padding:6px}
.submit{left:274px;top:848px;width:57px;height:18px;background:var(--teal);color:var(--white);font-size:12.5px;display:flex;align-items:center;justify-content:center}
.rev-btn{top:654px;width:22px;height:22px;background:#333;display:flex;align-items:center;justify-content:center}
.quote{left:345px;top:698px;width:291px;height:108px;border:1px solid #e2e2e2;border-radius:6px;padding:6px 14px 0 14px;font-size:7.8px;font-style:italic;line-height:14.8px;color:var(--text)}
.avatar{left:358px;top:794px;width:54px;height:54px;border-radius:50%;background:radial-gradient(circle at 50% 45%,#c98f70,#7a3a2a);border:3px solid #eee}
.reviewer{left:424px;top:827px;font-size:9.3px;color:var(--ink);font-weight:700}

/* franchise */
.franchise{left:0;top:884px;width:675px;height:128px;background:linear-gradient(100deg,#2b3036 0%,#4a5058 45%,#30353b 100%)}
.franchise-copy{left:40px;top:898px;width:595px;text-align:center;font-family:"Roboto Condensed",sans-serif;font-size:12.6px;line-height:22.4px;color:var(--white)}
.franchise-btn{left:206px;top:952px;width:240px;height:42px;border:1px solid var(--white);padding:3px}
.franchise-btn span{display:flex;width:100%;height:100%;background:var(--white);align-items:center;justify-content:center;font-family:"Roboto Slab",serif;color:var(--teal);font-size:19px}

/* footer */
.footer{left:0;top:1012px;width:675px;height:160px;background:var(--footer)}
.f-head{top:1025px;font-family:"Cinzel",serif;font-size:9.5px;color:var(--footer-text);padding-bottom:4px;border-bottom:1px solid #555}
.links{left:34px;top:1047px;list-style:none;font-size:8.3px;color:var(--footer-text);line-height:14px}
.links li{padding-left:10px;position:relative}
.links li::before{content:"";position:absolute;left:0;top:4px;border-left:3px solid var(--footer-text);border-top:2.5px solid transparent;border-bottom:2.5px solid transparent}
.map{left:162px;top:1050px;width:192px;height:99px;background:linear-gradient(135deg,#9cc0e6 0%,#c9d8c0 45%,#e8dcc0 60%,#8db5e0 100%)}
.vline{top:1030px;width:1px;height:130px;background:#4a4a4a}
.contact{left:394px;top:1049px;font-size:8.3px;line-height:12.5px;color:var(--footer-text)}
.contact p{margin-bottom:6px}
.foot-brand{left:534px;top:1098px;width:108px;text-align:center;font-family:"Arimo",Arial,sans-serif;font-weight:700;font-size:20px;line-height:24px;color:var(--footer-brand)}
.copyright{left:0;top:1172px;width:675px;height:28px;background:var(--teal);color:var(--white);font-size:7.5px;display:flex;align-items:center;justify-content:center}
</style>
</head>
<body>

<header>
  <div class="abs brand"><span class="brand-dot"></span>Calvexa</div>
  <div class="abs book-btn">Book An Appointment</div>
  <div class="abs call">
    <svg width="20" height="20" viewBox="0 0 20 20"><circle cx="10" cy="10" r="9" fill="none" stroke="#2ba6a0" stroke-width="1.3"/><path d="M7 5.5c-1 1-1 3 .8 5.6s3.8 3.8 5 3.4l1-1-1.8-1.6-1 .6c-.8-.4-2-1.8-2.4-2.6l.7-1L8 5z" fill="#2ba6a0"/></svg>
    <div class="call-text">Call Us Today<b>123-456-7890</b></div>
  </div>
</header>

<nav class="abs nav">
  <a class="active" style="left:30px;width:45px">Home</a>
  <a style="left:78px">Why Choose Us</a>
  <a style="left:186px">Treatable Conditions</a>
  <a style="left:332px">Testimonials</a>
  <a style="left:428px">FAQ's</a>
  <a style="left:482px">Franchising</a>
  <a style="left:573px;border:none">Contact Us</a>
</nav>

<section class="abs hero" role="img" aria-label="Photo of a therapist applying a laser device to a patient's back"></section>
<svg class="abs" style="left:10px;top:181px" width="16" height="20" viewBox="0 0 16 20"><path d="M12 2L4 10l8 8" fill="none" stroke="#fff" stroke-width="3"/></svg>
<svg class="abs" style="left:648px;top:181px" width="16" height="20" viewBox="0 0 16 20"><path d="M4 2l8 8-8 8" fill="none" stroke="#fff" stroke-width="3"/></svg>
<h1 class="abs hero-title">Back Pain Laser Therapy</h1>
<div class="abs hours"><h4>WORKING HOURS</h4><p>Monday-Friday 7:00 AM - 5:00 PM<br>Saturday &amp; Sunday Closed</p></div>

<section class="abs band">
  <svg class="abs" style="left:0;top:0" width="675" height="59"><path d="M198 0L174 59M385 0L361 59" stroke="rgba(255,255,255,.55)" stroke-width="1"/></svg>
  <div class="abs band-item" style="left:44px;top:16px">Check<br>Our Services</div>
  <svg class="abs" style="left:130px;top:14px" width="38" height="32" viewBox="0 0 38 32"><g stroke="#fff" stroke-width="1.6"><path d="M20 16L2 2M20 16l16-10M20 16l16 10M20 16l-6 14M20 16l8 14M20 16l-16 6M20 16V1"/></g><circle cx="20" cy="16" r="4" fill="#fff"/></svg>
  <div class="abs band-item serif" style="left:218px;top:17px">Book An<br>Appointment</div>
  <svg class="abs" style="left:324px;top:16px" width="26" height="28" viewBox="0 0 26 28"><path d="M4 8h14v16H4zM8 5v5M14 5v5" fill="none" stroke="#fff" stroke-width="1.6"/><path d="M12 18l4 4 8-12" fill="none" stroke="#fff" stroke-width="2"/></svg>
  <div class="abs band-item serif" style="left:399px;top:15px">Contact 123-456-7890<br>Street Name City Name State Zipcode</div>
  <svg class="abs" style="left:617px;top:15px" width="14" height="32" viewBox="0 0 14 32"><circle cx="7" cy="6" r="5.5" fill="none" stroke="#fff"/><path d="M5 3c-.6.6-.6 2 .6 3.4s2.4 2 3 1.8l.5-.6-1-.9-.6.4c-.5-.3-1.2-1-1.4-1.6l.4-.6z" fill="#fff"/><path d="M7 20a3 3 0 0 1 3 3c0 2-3 5-3 5s-3-3-3-5a3 3 0 0 1 3-3z" fill="#fff"/></svg>
</section>

<section>
  <h2 class="abs h2 rule" style="left:42px;top:396px;width:134px;padding-bottom:2px"><span class="first">About</span> Us</h2>
  <div class="abs about-copy">
    <p>Lorem ipsum dolor sit am sectetuer adipiscing elit, sed diam nonummy nibh euismod tincidunt ut laoreet dolore magna aliquam eravolutpat. Ut wisi enim ad minim veniam, quis nostrud exerci tation ullam corper suscipit lobortis nisl ut aliqu exreea commodo consequat. Duis autem vel eum iriure dolor facilisi.Lorems is the dummy text.</p>
    <p>Lorem ipsum dolor sit amsectetuer adipiscing elit, sed diam nonummy nibh euismod tincidunt ut laoreet dolore magna aliquam er.</p>
  </div>
  <a class="abs more" style="left:38px">Read More &gt;</a>

  <div class="abs photo" style="left:194px;background:linear-gradient(135deg,#6b3f22,#c98a62 55%,#e4d2b8)" role="img" aria-label="Photo of laser treatment on a patient's back"></div>
  <h3 class="abs service-title rule" style="left:195px"><span>Back</span> Pain</h3>
  <p class="abs service-text" style="left:195px">Lorem ipsum dolor sit ame rtetuer readipiscing elit, sed diam lorem onummy nibh euismod tincidunt Lorem ipsum dolor sit ame rtetue aoreet. dolor.</p>
  <a class="abs more" style="left:195px">Read More &gt;</a>

  <div class="abs photo" style="left:345px;background:linear-gradient(135deg,#2a3e5a,#5f7fa0 45%,#d8b49a)" role="img" aria-label="Photo of laser treatment on a patient's knee"></div>
  <h3 class="abs service-title rule" style="left:345px"><span>Knee</span> Pain</h3>
  <p class="abs service-text" style="left:345px">Lorem ipsum dolor sit ame rtetuer readipiscing elit, sed diam lorem onummy nibh euismod tincidunt Lorem ipsum dolor sit ame rtetue aoreet. dolor.</p>
  <a class="abs more" style="left:345px">Read More &gt;</a>

  <div class="abs photo" style="left:495px;background:linear-gradient(135deg,#d9dcdf,#e8c7a8 55%,#b07a50)" role="img" aria-label="Photo of laser treatment on a patient's shoulder"></div>
  <h3 class="abs service-title rule" style="left:495px"><span>Shoulder</span> Pain</h3>
  <p class="abs service-text" style="left:495px">Lorem ipsum dolor sit ame rtetuer readipiscing elit, sed diam lorem onummy nibh euismod tincidunt Lorem ipsum dolor sit ame rtetue aoreet. dolor.</p>
  <a class="abs more" style="left:495px">Read More &gt;</a>
</section>

<div class="abs divider"></div>

<section>
  <h2 class="abs h2" style="left:42px;top:649px;font-size:15px"><span class="first">Quick</span> Inquiry</h2>
  <p class="abs sub" style="left:42px;top:669px">Write to us</p>
  <div class="abs rule" style="left:36px;top:683px;width:295px"></div>
  <label class="abs label" style="left:36px;top:695px">First and last name*</label>
  <div class="abs field" style="left:36px;top:706px;width:143px;height:25px"></div>
  <label class="abs label" style="left:189px;top:695px">Your Email*</label>
  <div class="abs field" style="left:189px;top:706px;width:142px;height:25px"></div>
  <label class="abs label" style="left:36px;top:737px">Subject*</label>
  <div class="abs field" style="left:36px;top:748px;width:143px;height:25px"></div>
  <label class="abs label" style="left:189px;top:737px">Attach Photo*</label>
  <div class="abs field" style="left:189px;top:748px;width:142px;height:25px">Choose file</div>
  <label class="abs label" style="left:36px;top:779px">Description of a problem*</label>
  <div class="abs field" style="left:36px;top:791px;width:295px;height:50px"></div>
  <div class="abs submit">Submit</div>

  <h2 class="abs h2" style="left:344px;top:649px;font-size:15px"><span class="first">Customer</span> Reviews</h2>
  <p class="abs sub" style="left:346px;top:669px">What other said about us</p>
  <div class="abs rule" style="left:345px;top:683px;width:292px"></div>
  <div class="abs rev-btn" style="left:589px"><svg width="8" height="10"><path d="M6 1L2 5l4 4" fill="none" stroke="#fff" stroke-width="1.6"/></svg></div>
  <div class="abs rev-btn" style="left:614px"><svg width="8" height="10"><path d="M2 1l4 4-4 4" fill="none" stroke="#fff" stroke-width="1.6"/></svg></div>
  <div class="abs quote">
    <span style="font-size:20px;color:#bbb;font-style:normal;line-height:10px">&ldquo;</span> Fixed problem with heating system as requested. Performed inspection of car and found other issues that need attention now which we fixed and found other issues to be aware of but did not require immediate attention. (no pressure to have work done which was appreciated) <span style="font-size:20px;color:#bbb;font-style:normal">&rdquo;</span>
  </div>
  <div class="abs avatar" role="img" aria-label="Customer portrait"></div>
  <p class="abs reviewer">Mr.Owen Hartley</p>
</section>

<section class="abs franchise" role="img" aria-label="Background photo of a business handshake"></section>
<p class="abs franchise-copy">Lorem ipsum dolor sit amet, consectetuer adipiscing elit, sed diam nonummy nibh euismod tinciduntLorem ipsum dolor sit amet, consectetuer adipiscing elit, sed diam nonummy nibh.</p>
<div class="abs franchise-btn"><span>Become Our Franchise</span></div>

<footer>
  <div class="abs footer"></div>
  <h4 class="abs f-head" style="left:34px;width:89px">Quick Links</h4>
  <ul class="abs links">
    <li>Home</li><li>Why Choose Us</li><li>Treatable Conditions</li><li>Testimonials</li><li>FAQ's</li><li>Franchising</li><li>Contact Us</li>
  </ul>
  <div class="abs vline" style="left:142px"></div>
  <h4 class="abs f-head" style="left:161px;border:none">Our Location</h4>
  <div class="abs map" role="img" aria-label="Map showing the clinic location"></div>
  <div class="abs vline" style="left:370px"></div>
  <h4 class="abs f-head" style="left:394px;border:none">Contact Details</h4>
  <div class="abs contact">
    <p>Phone<br>123-456-7890</p>
    <p>Address<br>Street Name City Name<br>State Zipcode</p>
    <p>Open hours:<br>Monday to Friday 7am-5pm</p>
  </div>
  <div class="abs foot-brand">Calvexa</div>
  <div class="abs copyright">Copyright ©2015. Calvexa All Rights Reserved</div>
</footer>

</body>
</html>
```